Need a landing page design.

We are currently trying to develop a landing page for our www.brightoakwellness.example website.

Objective: To peak a level of interest in Medical Practices to sign up to our program and promote our line of vitamins and supplements. We will be concentrating on email marketing as well as fax or direct mail to drive medical facilities to our landing page.

Page requirements:
1. A slider on the top portion showing our line of products from the brightoakwellness.example website.
2. An "about us" area to explain who we are and what we offer.
3. An area for a grid so that we can show potential earnings for the practice as part of our program.
4. A Testimonial area for a couple of testimonials
5. A scroll area where they can see our contract
6. A lead capture area where they can input their contact information so we may gather it and contact them back to explain the program. In this area I need the following fields: Name of Practice; Contact name; Email address; Phone Number; Area of Medical Discipline; Number of patients per day.
7. A nice clean contact us area

Other than these main requirements the rest is up to you.

Goal: Entice Medical practices to use our FREE service to increase revenue for their offices while helping their patients save money on their supplements.

Key Factors for the Medical facility to know: Free to sign up, no inventory carrying costs. Simple backend sales area to process orders. We handle all shipping and customer service.

Thank you

Target Market(s)

Medical Facilities, mainly office managers and docotors

Industry/Entity Type

Marketing

Requirements
Must have
• Professional design as we are dealing with the medical field.

```html
<!DOCTYPE html>
<html lang="en">
<head>
<meta charset="utf-8">
<title>Bright Oak Wellness – Practice Program</title>
<link href="https://fonts.googleapis.com/css2?family=Signika:wght@300;400;600&family=PT+Sans:wght@400;700&display=swap" rel="stylesheet">
<style>
:root{
  --brown:#5a3f2c;
  --brown-dark:#3f2a1c;
  --teal:#3fb3c4;
  --teal-light:#7fd3de;
  --teal-dark:#2f9db0;
  --text:#4a4a4a;
  --muted:#6d6d6d;
  --grey:#e6e6e6;
  --line:#dcdcdc;
  --white:#fff;
  --star:#3a8fd0;
}
*{box-sizing:border-box;margin:0;padding:0}
html,body{width:786px;height:1200px;overflow:hidden}
body{position:relative;background:var(--white);font-family:"PT Sans",sans-serif;color:var(--text);font-size:8px}
h1,h2,h3{font-weight:400}
.abs{position:absolute}
.topline{left:0;top:0;width:786px;height:4px;background:var(--brown)}
.backdrop{left:0;top:4px;width:786px;height:290px;background:linear-gradient(90deg,#bfe6ec 0%,#e8f6f8 30%,#f4f7f2 55%,#e7d6bd 80%,#d9a86b 100%)}
.backdrop-low{left:0;top:150px;width:786px;height:144px;background:linear-gradient(180deg,rgba(63,179,196,0) 0%,rgba(63,179,196,.7) 100%)}
.logo{left:70px;top:14px;width:76px;height:76px;border-radius:50%;background:var(--teal-light);border:3px solid var(--white);box-shadow:0 0 0 2px #b9a88f;display:flex;align-items:center;justify-content:center;text-align:center;font-family:"Signika",sans-serif;font-size:10px;color:var(--white);line-height:1.1}
.account{left:526px;top:0;width:201px;height:34px;background:var(--brown);border-radius:0 0 6px 6px;color:var(--white);font-size:9px;display:flex;align-items:center;justify-content:space-around;padding:0 10px}
.account span::before{content:"";display:inline-block;width:8px;height:8px;border-radius:50%;background:var(--white);margin-right:3px;vertical-align:-1px}
.phone{left:605px;top:42px;font-family:"Signika",sans-serif;font-size:17px;color:var(--brown-dark)}
.phone svg{vertical-align:-2px;margin-right:3px}
.search{left:554px;top:70px;width:168px;height:18px;border-radius:9px;background:var(--white);border:1px solid var(--line);font-size:7px;font-style:italic;color:#999;padding:4px 9px}
.search svg{position:absolute;right:7px;top:4px}
.nav{left:64px;top:97px;width:458px;height:34px;background:var(--brown);display:flex;align-items:center;padding-left:22px;gap:35px;font-family:"Signika",sans-serif;font-size:11.5px;color:var(--white)}
.hero{left:64px;top:131px;width:458px;height:226px;background:linear-gradient(135deg,#8ccbe6 0%,#c9e4ef 45%,#e9c8a6 70%,#3b7fb8 100%)}
.caption{left:75px;top:274px;width:203px;height:83px;background:rgba(90,63,44,.9);color:var(--white);padding:7px 15px;font-family:"Signika",sans-serif}
.caption .small{font-size:13px;font-weight:300}
.caption .big{font-size:18px;font-weight:600;line-height:1.15}
.dots{left:370px;top:337px;display:flex;gap:4px}
.dots i{width:7px;height:7px;border-radius:50%;background:rgba(255,255,255,.8)}
.form{left:522px;top:100px;width:200px;height:257px;background:var(--white);border:1px solid var(--line)}
.form-head{left:522px;top:100px;width:200px;height:31px;background:var(--teal);color:var(--white);font-family:"Signika",sans-serif;font-size:14px;padding:6px 17px}
.field{left:538px;width:143px;height:21px;border:1px solid #cfcfcf;border-radius:2px;background:var(--white);font-size:7.5px;color:#666;padding:5px 8px}
.submit{left:630px;top:317px;width:74px;height:20px;background:var(--brown);color:var(--white);font-family:"Signika",sans-serif;font-weight:600;font-size:8px;text-align:center;padding-top:5px;border-radius:2px}
.welcome{left:64px;top:376px;font-size:17px;color:var(--teal-dark);font-family:"Signika",sans-serif;font-weight:400}
.lead{left:65px;top:406px;font-size:9.3px;color:#333}
.intro{left:65px;top:425px;width:450px;font-size:7.8px;line-height:16px;color:var(--muted)}
.col-title{font-family:"Signika",sans-serif;font-weight:300;font-size:13.5px;color:var(--brown-dark)}
.col-text{font-size:7.8px;line-height:15.6px;color:var(--muted);margin-top:6px;white-space:nowrap}
.divider{left:286px;top:465px;width:1px;height:105px;background:var(--line)}
.under{left:287px;top:568px;width:230px;height:1px;background:var(--line)}
.latest{left:64px;top:581px;font-size:16px;color:var(--teal-dark);font-family:"Signika",sans-serif;font-weight:300}
.card{width:141px;height:175px;border:1px solid var(--line);background:var(--white)}
.card .stars{position:absolute;left:8px;top:4px;font-size:10px;letter-spacing:2px;color:var(--star)}
.card .stars b{color:#ccc;font-weight:400}
.card .shot{position:absolute;left:45px;top:20px;width:50px;height:90px;border-radius:8px}
.card .info{position:absolute;left:0;bottom:0;width:139px;height:58px;background:var(--grey);padding:6px 9px}
.card .name{font-family:"Signika",sans-serif;font-weight:400;font-size:10.5px;color:#444}
.card .price{font-size:7px;line-height:13px;color:#666;margin-top:1px}
.card .cart{position:absolute;right:6px;bottom:8px;width:49px;height:16px;background:var(--teal);border-radius:2px;color:var(--white);font-size:6.8px;text-align:center;padding-top:3px}
.contract{left:526px;top:371px;width:196px;height:124px;border:1px solid var(--line)}
.contract-head{left:527px;top:372px;width:194px;height:31px;background:#f0f0f0;font-family:"Signika",sans-serif;font-weight:400;font-size:14px;color:var(--brown-dark);padding:6px 12px}
.scroll-btn{left:683px;top:377px;width:23px;height:21px;border-radius:50%;background:var(--teal-light);color:var(--white);font-size:9px;text-align:center;padding-top:4px}
.partner{left:527px;top:403px;width:194px;height:91px;display:flex;align-items:center;justify-content:center;font-family:"Signika",sans-serif;font-weight:300;font-size:16px;color:#222}
.testi-title{left:528px;top:512px;font-size:17px;color:var(--brown-dark);font-family:"Signika",sans-serif;font-weight:300}
.avatar{width:64px;height:64px;border-radius:50%;border:3px solid var(--white);box-shadow:0 0 0 1px #ccc}
.quote{font-size:8px;font-style:italic;line-height:15.6px;color:#555;white-space:nowrap}
.quote::before{content:"\201C";position:absolute;left:-4px;top:-12px;font-size:20px;color:#ccc;font-style:normal}
.quote::after{content:"\201D";position:absolute;right:-16px;bottom:-14px;font-size:20px;color:#ccc;font-style:normal}
.who{width:200px;text-align:right;font-size:7.3px;line-height:16px;color:#555}
.earn{left:526px;top:774px;width:196px;height:203px;border:1px solid var(--line)}
.earn-head{left:526px;top:774px;width:196px;height:57px;background:linear-gradient(#f2f2f2,#e0e0e0);font-family:"Signika",sans-serif;font-weight:300;font-size:16px;color:var(--brown-dark);padding:10px 19px;line-height:1.15}
.earn-shot{left:543px;top:843px;width:68px;height:58px;background:linear-gradient(135deg,#2a6fa8,#56a7d6 60%,#1d4f7c)}
.earn-title{left:620px;top:843px;font-family:"Signika",sans-serif;font-weight:400;font-size:11.5px;color:#333}
.earn-text{font-size:8px;line-height:14.3px;color:#666;white-space:nowrap}
.learn{left:545px;top:953px;width:59px;height:18px;background:var(--teal);color:var(--white);font-family:"Signika",sans-serif;font-weight:600;font-size:7.5px;text-align:center;padding-top:4px;border-radius:2px}
.footer{left:0;top:980px;width:786px;height:172px;background:linear-gradient(180deg,#8fd8e1 0%,#5cc3d1 100%)}
.footer-bottom{left:0;top:1152px;width:786px;height:41px;background:var(--teal-dark)}
.bottomline{left:0;top:1193px;width:786px;height:7px;background:var(--brown)}
.f-title{top:1008px;font-family:"Signika",sans-serif;font-weight:300;font-size:14px;color:var(--white)}
.f-list{top:1034px;list-style:none;font-size:8.2px;line-height:15.6px;color:var(--white)}
.social{left:551px;top:1034px;display:flex;gap:4px}
.social i{width:22px;height:22px;border-radius:50%;background:var(--white)}
.copy{left:62px;top:1169px;font-size:8px;color:var(--white)}
.mark{left:691px;top:1171px;font-size:7px;color:#d9f2f5}
</style>
</head>
<body>
<div class="abs topline"></div>
<div class="abs backdrop" role="img" aria-label="Soft sunny sky backdrop with wheat field edge"></div>
<div class="abs backdrop-low"></div>

<div class="abs logo">Bright Oak<br>Wellness</div>

<div class="abs account"><span>My Account</span><span>Checkout</span><span>Login</span></div>
<div class="abs phone"><svg width="14" height="14" viewBox="0 0 24 24"><path d="M6.6 10.8a15 15 0 0 0 6.6 6.6l2.2-2.2c.3-.3.7-.4 1-.2 1.1.4 2.3.6 3.6.6.6 0 1 .4 1 1V20c0 .6-.4 1-1 1A17 17 0 0 1 3 4c0-.6.4-1 1-1h3.5c.6 0 1 .4 1 1 0 1.3.2 2.5.6 3.6.1.3 0 .7-.2 1z" fill="#8cc9d9"/></svg>1800.555.014</div>
<div class="abs search">Search here..<svg width="10" height="10" viewBox="0 0 10 10"><circle cx="4" cy="4" r="3" fill="none" stroke="#777" stroke-width="1.3"/><path d="M6.3 6.3 9 9" stroke="#777" stroke-width="1.5"/></svg></div>

<nav class="abs nav"><span>HOME</span><span>ABOUT US</span><span>PRODUCTS</span><span>CONTACT US</span><span>SIGN IN</span></nav>

<div class="abs hero" role="img" aria-label="Smiling couple outdoors beside a blue supplement bottle"></div>
<div class="abs caption"><div class="small">SMART AND SUSTAINABLE</div><div class="big">INCREASE SEX<br>DRIVE &amp; STAMINA</div></div>
<div class="abs dots"><i></i><i></i><i></i><i></i></div>

<div class="abs form"></div>
<div class="abs form-head">Fill Our Contact Form</div>
<div class="abs field" style="top:148px">Name of Practice</div>
<div class="abs field" style="top:175px">Contact name</div>
<div class="abs field" style="top:204px">Email address</div>
<div class="abs field" style="top:232px">Phone Number</div>
<div class="abs field" style="top:260px">Area of Medical Discipline</div>
<div class="abs field" style="top:288px;left:540px;width:165px">Number of patients per day<svg style="position:absolute;right:7px;top:8px" width="7" height="5" viewBox="0 0 7 5"><path d="M0 0h7L3.5 5z" fill="#222"/></svg></div>
<div class="abs submit">SUBMIT NOW</div>

<h1 class="abs welcome">Welcome to Our Website Mainpage</h1>
<p class="abs lead">Nunc tempus felis vitae urna Vivamus porttitor purus nisi eleifend libero, a tempus</p>
<p class="abs intro">Phasellus felis dolor, scelerisque a, tempus eget, lobortis id, libero. Donec scelerisque leo ac risus. Praesent sit amet est.<br>In dictum, dolor eu dictum porttitor, enim felis viverra mi, eget luctus massa purus quis odio.</p>

<section class="abs" style="left:70px;top:468px">
  <h2 class="col-title">Who we are</h2>
  <p class="col-text">Duis tincidunt lectus quis dui viverra vestibulum.<br>Suspendisse vulputate aliquam dui. Nulla elementum<br>dui ut augue. Aliquam vehicula mi at mauris.<br>Maecenas placerat nisl at</p>
</section>
<div class="abs divider"></div>
<section class="abs" style="left:296px;top:468px">
  <h2 class="col-title">What we offer</h2>
  <p class="col-text">Duis tincidunt lectus quis dui viverra vestibulum.<br>Suspendisse vulputate aliquam dui. Nulla elementum<br>dui ut augue. Aliquam vehicula mi at mauris.<br>Maecenas placerat nisl at</p>
</section>
<div class="abs under"></div>

<h2 class="abs latest">Latest Products</h2>

<div class="abs card" style="left:65px;top:606px"><div class="stars">★★★★<b>★</b></div><div class="shot" style="background:linear-gradient(90deg,#ddd,#b08a60,#ddd)" role="img" aria-label="Supplement tub"></div><div class="info"><div class="name">Product Name</div><div class="price">Easy Auto Ship: $33.25<br>Regular Price: $39.95</div><div class="cart">Add to Cart</div></div></div>
<div class="abs card" style="left:213px;top:606px"><div class="stars">★★★★<b>★</b></div><div class="shot" style="background:linear-gradient(90deg,#1d5f98,#4fa4d8,#1d5f98)" role="img" aria-label="Blue supplement bottle"></div><div class="info"><div class="name">Product Name</div><div class="price">Easy Auto Ship: $33.25<br>Regular Price: $39.95</div><div class="cart">Add to Cart</div></div></div>
<div class="abs card" style="left:362px;top:606px"><div class="stars">★★★★<b>★</b></div><div class="shot" style="background:linear-gradient(90deg,#1a1f33,#4a5375,#1a1f33)" role="img" aria-label="Dark supplement bottle"></div><div class="info"><div class="name">Product Name</div><div class="price">Easy Auto Ship: $33.25<br>Regular Price: $39.95</div><div class="cart">Add to Cart</div></div></div>
<div class="abs card" style="left:65px;top:796px"><div class="stars">★★★★<b>★</b></div><div class="shot" style="background:linear-gradient(90deg,#ddd,#b08a60,#ddd)" role="img" aria-label="Supplement tub"></div><div class="info"><div class="name">Product Name</div><div class="price">Easy Auto Ship: $33.25<br>Regular Price: $39.95</div><div class="cart">Add to Cart</div></div></div>
<div class="abs card" style="left:213px;top:796px"><div class="stars">★★★★<b>★</b></div><div class="shot" style="background:linear-gradient(90deg,#1d5f98,#4fa4d8,#1d5f98)" role="img" aria-label="Blue supplement bottle"></div><div class="info"><div class="name">Product Name</div><div class="price">Easy Auto Ship: $33.25<br>Regular Price: $39.95</div><div class="cart">Add to Cart</div></div></div>
<div class="abs card" style="left:362px;top:796px"><div class="stars">★★★★<b>★</b></div><div class="shot" style="background:linear-gradient(90deg,#1a1f33,#4a5375,#1a1f33)" role="img" aria-label="Dark supplement bottle"></div><div class="info"><div class="name">Product Name</div><div class="price">Easy Auto Ship: $33.25<br>Regular Price: $39.95</div><div class="cart">Add to Cart</div></div></div>

<div class="abs contract"></div>
<h2 class="abs contract-head">Our Contract</h2>
<div class="abs scroll-btn">‹›</div>
<div class="abs partner">Clearpath Health</div>

<h2 class="abs testi-title">Testimonials</h2>
<div class="abs avatar" style="left:532px;top:542px;background:linear-gradient(#6b4a35,#c99b7c)" role="img" aria-label="Portrait of a male client"></div>
<p class="abs quote" style="left:601px;top:553px">Sed ut perspiciatis unde omnis<br>iste natus error sit voluptatem<br>accusantium doloremque l</p>
<p class="abs who" style="left:501px;top:612px">- Daniel Moreau,<br>Project Manger for Linwood and Partners</p>
<div class="abs avatar" style="left:532px;top:664px;background:linear-gradient(#8b4a2e,#e0b196)" role="img" aria-label="Portrait of a female client"></div>
<p class="abs quote" style="left:603px;top:666px">Sed ut perspiciatis unde omnis<br>iste natus error sit voluptatem<br>accusantium doloremque l</p>
<p class="abs who" style="left:503px;top:733px">- Daniel Moreau,<br>Project Manger for Linwood and Partners</p>

<div class="abs earn"></div>
<h2 class="abs earn-head">Potential Earnings for<br>the Practice</h2>
<div class="abs earn-shot" role="img" aria-label="Supplement bottles"></div>
<div class="abs earn-title">Duis tincidunt</div>
<p class="abs earn-text" style="left:620px;top:858px">quis dui viverra<br>vestibulum. Suspend<br>isse vulputate aliquam</p>
<p class="abs earn-text" style="left:545px;top:903px">quis dui viverra vestibulum. Suspend isse<br>vulputate aliquam dui. Nulla elementum<br>dui ut augue Aliquam</p>
<div class="abs learn">LEARN MORE</div>

<footer>
<div class="abs footer"></div>
<h3 class="abs f-title" style="left:66px">Quick Links</h3>
<ul class="abs f-list" style="left:69px"><li>Home</li><li>About Us</li><li>Products</li><li>Contact Us</li><li>Become an Affiliate</li><li>Become a Reseller</li></ul>
<h3 class="abs f-title" style="left:190px">Terms and Conditions</h3>
<ul class="abs f-list" style="left:193px"><li>Privacy Policy</li><li>Return Policy</li><li>Terms and Conditions</li><li>Contact Us</li></ul>
<h3 class="abs f-title" style="left:367px">Contact Information</h3>
<ul class="abs f-list" style="left:370px;top:1032px"><li style="font-size:9.5px">Bright Oak Wellness</li><li>42 Harbor Lane #2B</li><li>Springfield 01105 MA</li><li>Phone no. <span style="font-size:11px">888-555-0192</span></li><li>Email add: info@brightoakwellness.example</li></ul>
<h3 class="abs f-title" style="left:547px">Get Connected</h3>
<div class="abs social"><i></i><i></i><i></i><i></i></div>
<div class="abs footer-bottom"></div>
<p class="abs copy">Copyright © 2013 Company Name.&nbsp; All right reserved.</p>
<p class="abs mark">M1</p>
<div class="abs bottomline"></div>
</footer>
</body>
</html>
```